CD-/Plattencover für Gothic Rockband
Zielgruppe
Wir sind eine Gothic Rockband und suchen für unser neues Studioalbum ein CD-Cover OHNE Booklet, etc.
Aufgabenstellung
Der Albumtitel lautet: VERMARA
Der Albumtitelschriftzug sollte ungefähr in dem Design sein, das wir mit beigefügt haben.
Das Artwork sollte einen starken Gothicbezug haben, also gerne mystisch, geheimnisvoll. Evtl. ein menschlicher Protagonist im Vordergrund, ist aber kein Muss.
Der Bandname braucht nicht auf dem Cover zu sein, diesen setzen wir später selber ein.

```html
<!DOCTYPE html>
<html lang="de">
<head>
<meta charset="utf-8">
<title>VERMARA – Albumcover</title>
<link rel="stylesheet" href="https://fonts.googleapis.com/css2?family=Cinzel+Decorative:wght@900&display=swap">
<style>
  :root {
    --night: #040404;
    --ash: #3c3c3c;
    --smoke: #8a8a8a;
    --ember: #f4b457;
    --flare: #d8362a;
    --title-top: #4a4744;
    --title-bottom: #070707;
    --title-edge: #b89868;
  }
  html, body {
    margin: 0;
    padding: 0;
    width: 1200px;
    height: 1199px;
    overflow: hidden;
    background: var(--night);
  }
  .cover {
    position: relative;
    width: 1200px;
    height: 1199px;
    overflow: hidden;
    background: var(--night);
  }
  .cover-artwork {
    position: absolute;
    inset: 0;
    background:
      linear-gradient(178deg, transparent 21.5%, rgba(244,180,87,0.85) 23.5%, rgba(255,230,170,0.9) 24.3%, rgba(216,54,42,0.7) 26%, rgba(216,54,42,0.25) 28.5%, transparent 31%),
      radial-gradient(ellipse 22% 30% at 50% 47%, rgba(210,210,210,0.55) 0%, rgba(120,120,120,0.35) 45%, transparent 100%),
      radial-gradient(ellipse 20% 45% at 11% 55%, rgba(200,200,200,0.6) 0%, rgba(110,110,110,0.4) 50%, transparent 100%),
      radial-gradient(ellipse 10% 8% at 17% 17%, rgba(190,190,190,0.55) 0%, transparent 100%),
      radial-gradient(ellipse 30% 30% at 82% 65%, rgba(90,90,90,0.5) 0%, transparent 100%),
      radial-gradient(ellipse 25% 25% at 20% 92%, rgba(150,150,150,0.45) 0%, transparent 100%),
      linear-gradient(180deg, #000 0%, #0c0c0c 8%, #1c1c1c 16%, #262626 22%, #1e1e1e 32%, var(--ash) 50%, #2c2c2c 75%, #2a2a2a 100%);
  }
  .album-title {
    position: absolute;
    left: 0;
    top: 0;
    width: 1200px;
    height: 1199px;
    pointer-events: none;
  }
  .album-title text {
    font-family: "Cinzel Decorative", serif;
    font-weight: 900;
    font-size: 300px;
    fill: url(#title-bevel);
    stroke: var(--title-edge);
    stroke-width: 4px;
    paint-order: stroke;
  }
</style>
</head>
<body>
  <main class="cover">
    <div class="cover-artwork" role="img" aria-label="Schwarzweiß-Fotocollage: ein Mann mit Sonnenbrille im Vordergrund links, ein kopfstehendes Wohnhaus, Baumspiegelungen und orange-rote Lichtspuren einer nächtlichen Straße"></div>
    <svg class="album-title" viewBox="0 0 1200 1199" aria-label="VERMARA">
      <defs>
        <linearGradient id="title-bevel" x1="0" y1="0" x2="0" y2="1">
          <stop offset="0" stop-color="var(--title-top)"/>
          <stop offset="0.45" stop-color="#1a1918"/>
          <stop offset="1" stop-color="var(--title-bottom)"/>
        </linearGradient>
        <filter id="title-shadow" x="-5%" y="-10%" width="110%" height="130%">
          <feDropShadow dx="4" dy="6" stdDeviation="5" flood-color="#000" flood-opacity="0.85"/>
        </filter>
      </defs>
      <g filter="url(#title-shadow)" transform="translate(0 1040) scale(1 1.42)">
        <text x="42" y="0" textLength="1110" lengthAdjust="spacingAndGlyphs">VERMARA</text>
      </g>
    </svg>
  </main>
</body>
</html>
```